Business Card Design

Need a card designed to fit the tax preparation and accounting profession. Would like to include the following on side two of the card:

Tax Preparation and Audit Representation for:
Individuals
Partnerships
Corporations
Estates
Trusts
Other entities with tax reporting requirements

Industry/Entity Type

Accounting

Contact Information for Business Card

Whitcombe & Associates
Tax and Business Services
Gerald R Whitcombe III, EA, MS
Enrolled Agent P08637519
4172 Marrowind Lane, Suite B
Alder Springs, CA 95804
(916) 482-6157
Email: ledgerpro729@mailbrook.example
www.ledgerhelpdesk.example

```html
<!DOCTYPE html>
<html lang="en">
<head>
<meta charset="utf-8">
<title>Whitcombe &amp; Associates — Business Card</title>
<link rel="stylesheet" href="https://fonts.googleapis.com/css2?family=Bodoni+Moda:wght@400;500&family=Cabin+Condensed:wght@400&family=Arimo:wght@400&family=Open+Sans:wght@400&display=swap">
<style>
  :root {
    --page: #ffffff;
    --card: #242424;
    --card-light: #3a3a3a;
    --accent: #27a2d8;
    --text: #f2f2f2;
    --muted: #c9c9c9;
    --rule: #8a8a8a;
    --frame: #5b5b5b;
  }
  * { margin: 0; padding: 0; box-sizing: border-box; }
  html, body { width: 1200px; height: 1000px; overflow: hidden; background: var(--page); }
  .canvas { position: relative; width: 1200px; height: 1000px; }

  .card {
    position: absolute;
    overflow: hidden;
    background:
      radial-gradient(ellipse at 50% 40%, var(--card-light) 0%, var(--card) 70%),
      var(--card);
    color: var(--text);
  }
  .card--front { left: 230px; top: 38px; width: 731px; height: 425px; }
  .card--back  { left: 236px; top: 502px; width: 748px; height: 435px; box-shadow: 0 -6px 18px rgba(0,0,0,0.08); }

  .accent-bar { position: absolute; background: var(--accent); }

  .brand {
    position: absolute; left: 0; right: 0; top: 110px;
    text-align: center; white-space: nowrap;
    font-family: "Bodoni Moda", "Didot", serif;
    font-size: 48px; font-weight: 400; line-height: 1;
    color: var(--text);
  }
  .brand__accent { color: var(--accent); }
  .tagline {
    position: absolute; left: 0; right: 0; top: 172px;
    text-align: center; white-space: nowrap;
    font-family: "Cabin Condensed", "Arial Narrow", sans-serif;
    font-size: 50px; font-variant: small-caps; line-height: 1;
    color: var(--text);
  }
  .services-heading {
    position: absolute; left: 0; right: 0; top: 307px;
    text-align: center; white-space: nowrap;
    font-family: "Arimo", Arial, sans-serif;
    font-size: 21.5px; letter-spacing: 0.3px; color: var(--text);
  }
  .services-rule { position: absolute; left: 56px; width: 615px; top: 336px; height: 2px; background: var(--text); }
  .services-list {
    position: absolute; left: 0; right: 0; top: 346px;
    text-align: center; white-space: nowrap;
    font-family: "Arimo", Arial, sans-serif;
    font-size: 19.5px; line-height: 22px; letter-spacing: 0.3px; color: var(--text);
  }

  .portrait-frame {
    position: absolute; left: 96px; top: 66px; width: 214px; height: 199px;
    background: var(--frame); border-radius: 8px;
    box-shadow: 0 0 40px rgba(0,0,0,0.8);
    padding: 8px;
  }
  .portrait {
    width: 100%; height: 100%;
    background: linear-gradient(120deg, #8d9bd3 0%, #e9c7c4 45%, #3b2a24 70%, #1e1e22 100%);
  }
  .holder-name {
    position: absolute; left: 20px; width: 356px; top: 288px;
    text-align: center; white-space: nowrap;
    font-family: "Bodoni Moda", "Didot", serif;
    font-size: 27px; line-height: 1; color: var(--muted);
  }
  .holder-name__accent { color: var(--accent); }

  .divider { position: absolute; left: 366px; top: 182px; width: 1px; height: 171px; background: var(--rule); }
  .contact {
    position: absolute; left: 376px; top: 180px;
    font-family: "Open Sans", Arial, sans-serif;
    font-size: 16px; color: var(--text); white-space: nowrap;
  }
  .contact__address { line-height: 23px; text-transform: uppercase; margin-bottom: 14px; }
  .contact__list { list-style: none; }
  .contact__item { position: relative; padding-left: 24px; line-height: 30px; }
  .contact__item::before {
    content: ""; position: absolute; left: 4px; top: 11px;
    width: 10px; height: 10px; background: var(--accent);
  }
</style>
</head>
<body>
<div class="canvas">

  <section class="card card--front">
    <div class="accent-bar" style="left:0; top:127px; width:35px; height:172px;"></div>
    <div class="accent-bar" style="left:695px; top:127px; width:36px; height:172px;"></div>
    <h1 class="brand">Whitcombe <span class="brand__accent">&amp; Associates</span></h1>
    <p class="tagline">Tax and Business Services</p>
    <p class="services-heading">TAX PREPARATION AND AUDIT REPRESENTATION FOR:</p>
    <div class="services-rule"></div>
    <p class="services-list">INDIVIDUALS / PARTNERSHIPS / TRUSTS / CORPORATIONS / ESTATES<br>OTHER ENTITIES WITH TAX REPORTING REQUIREMENTS</p>
  </section>

  <section class="card card--back">
    <div class="accent-bar" style="left:1px; top:184px; width:35px; height:107px;"></div>
    <div class="accent-bar" style="left:711px; top:187px; width:37px; height:101px;"></div>
    <div class="portrait-frame">
      <div class="portrait" role="img" aria-label="Portrait photo of the tax professional in a suit in front of an American flag"></div>
    </div>
    <p class="holder-name">Gerald <span class="holder-name__accent">R Whitcombe III</span></p>
    <div class="divider"></div>
    <div class="contact">
      <p class="contact__address">P08637519 4172 Marrowind Lane,<br>Suite B Alder Springs, CA 95804</p>
      <ul class="contact__list">
        <li class="contact__item">Contact :- (916) 482-6157</li>
        <li class="contact__item">Email: ledgerpro729@mailbrook.example</li>
        <li class="contact__item">www.ledgerhelpdesk.example</li>
      </ul>
    </div>
  </section>

</div>
</body>
</html>
```